Dean harlow realestate

We want something complete different to our website now and something that will stand out this is our website http://deanharlowrealestate-example.com/

our company website for my boss is www.trevorvance-example.com

please note this website is being made for dean harlow not trevor vance

something similar to our company website but has to be in the branding of dean harlow realestate

```html
<!DOCTYPE html>
<html lang="en">
<head>
<meta charset="utf-8">
<title>Dean Harlow Property</title>
<link href="https://fonts.googleapis.com/css2?family=Roboto:wght@400;500;700;900&family=Raleway:wght@600;700&display=swap" rel="stylesheet">
<style>
:root{
  --navy:#1d2b4f;
  --navy-deep:#16223f;
  --orange:#f36c0f;
  --ink:#222;
  --muted:#777;
  --light:#f3f3f3;
  --white:#fff;
  --footer:#1b1b1b;
}
*{box-sizing:border-box;margin:0;padding:0}
html,body{width:1200px;height:3193px;overflow:hidden}
body{font-family:'Roboto',sans-serif;color:var(--ink);background:var(--light);position:relative}

/* header */
.site-header{position:absolute;left:0;top:0;width:1200px;height:80px;background:var(--navy);z-index:3}
.brand{position:absolute;left:133px;top:27px;display:flex;align-items:center;gap:9px;color:var(--white);font-size:19px;font-weight:500}
.brand-mark{width:12px;height:12px;background:var(--orange)}
.main-nav{position:absolute;left:480px;top:0;display:flex;height:62px}
.main-nav a{color:var(--white);text-decoration:none;font-size:11px;font-weight:700;padding:0 14px;display:flex;align-items:center;text-transform:uppercase}
.main-nav a.active{background:var(--orange);border-radius:0 0 10px 10px}
.phone-pill{position:absolute;left:920px;top:23px;width:146px;height:32px;border-radius:16px;background:var(--orange);color:var(--white);font-weight:700;font-size:15px;display:flex;align-items:center;justify-content:center;gap:8px}

/* hero */
.hero{position:absolute;left:0;top:80px;width:1200px;height:495px;
  background:
    radial-gradient(ellipse 420px 260px at 600px 250px,rgba(40,48,66,.85),rgba(40,48,66,0) 70%),
    radial-gradient(ellipse 130px 60px at 930px 420px,rgba(235,170,70,.55),rgba(235,170,70,0) 70%),
    linear-gradient(180deg,#7d8ca3 0%,#5a6881 35%,#3c4252 65%,#4d4640 85%,#5f5a4c 100%)}
.hero-eyebrow{position:absolute;top:190px;width:100%;text-align:center;color:var(--white);font-weight:700;font-size:15px;letter-spacing:.5px}
.hero-title{position:absolute;top:208px;width:100%;text-align:center;color:var(--white);font-weight:700;font-size:56px}
.hero-btn{position:absolute;left:540px;top:297px;width:128px;height:34px;border:2px solid var(--white);border-radius:17px;color:var(--white);font-size:14px;font-weight:700;display:flex;align-items:center;justify-content:center}
.hero-arrow{position:absolute;top:200px}
.hero-dots{position:absolute;top:420px;left:580px;display:flex;gap:16px}
.hero-dots span{width:7px;height:7px;border-radius:50%;background:#ccc}
.hero-dots span.on{background:var(--orange)}

/* appraisal form */
.appraisal{position:absolute;left:133px;top:533px;width:934px;height:134px;background:var(--navy);padding:20px 24px;z-index:2}
.fields{display:grid;grid-template-columns:repeat(3,222px);gap:20px 24px}
.field{height:38px;background:var(--white);font-size:11px;color:#999;padding:0 14px;display:flex;align-items:center}
.appraisal-btn{position:absolute;right:21px;top:18px;width:150px;height:98px;background:var(--orange);color:var(--white);font-weight:700;font-size:12px;text-align:center;display:flex;flex-direction:column;align-items:center;justify-content:center;gap:8px}

/* properties */
.section-title{position:absolute;width:100%;text-align:center;font-weight:700;font-size:15px;text-transform:uppercase;color:var(--ink)}
.card{position:absolute;width:456px;height:347px;background:var(--white)}
.card-photo{height:244px}
.photo-patio{background:
  linear-gradient(180deg,rgba(255,255,255,0) 60%,rgba(0,0,0,.15) 100%),
  linear-gradient(90deg,#d6c79a 0%,#e2cf8f 35%,#8d8576 55%,#b9b3a7 100%)}
.photo-white{background:
  linear-gradient(180deg,#3e7cc3 0%,#6ea0d4 28%,#e7eaee 32%,#dadfe4 70%,#7e807f 72%,#9a9b98 100%)}
.photo-glass{background:
  linear-gradient(180deg,#2e73c2 0%,#5b95d2 30%,rgba(0,0,0,0) 31%),
  linear-gradient(90deg,#e9eaec 0%,#dfe2e5 40%,#3c4048 48%,#565a62 80%,#e5e6e8 100%)}
.photo-kitchen{background:
  linear-gradient(180deg,#f1f0ee 0%,#e7e5e1 45%,#c8c4bd 60%,#eeeceb 62%,#a9a49c 100%)}
.card-body{padding:14px 10px 0 10px;position:relative}
.card-name{font-size:10px;font-weight:700}
.card-price{position:absolute;right:10px;top:14px;font-size:10px;font-weight:700;color:var(--orange)}
.card-addr{font-size:10px;color:var(--muted);margin-top:4px;display:flex;align-items:center;gap:4px}
.card-feats{display:flex;gap:20px;margin-top:22px;font-size:11px;color:var(--muted)}
.card-feats span{display:flex;align-items:center;gap:6px}
.card-btn{position:absolute;right:10px;top:48px;width:98px;height:26px;border-radius:13px;background:var(--orange);color:var(--white);font-size:10px;display:flex;align-items:center;justify-content:center}
.load-more{position:absolute;left:511px;top:1487px;width:189px;height:36px;background:var(--orange);color:var(--white);font-size:11px;font-weight:700;display:flex;align-items:center;justify-content:center}

/* agent */
.agent{position:absolute;left:0;top:1553px;width:1200px;height:418px;background:
  radial-gradient(ellipse 300px 420px at 120px 200px,rgba(120,140,180,.35),rgba(0,0,0,0) 70%),
  linear-gradient(90deg,#2a3a62 0%,var(--navy) 45%,var(--navy-deep) 100%)}
.agent-photo{position:absolute;left:150px;top:30px;width:270px;height:388px;background:
  radial-gradient(ellipse 70px 85px at 135px 110px,rgba(220,170,140,.55),rgba(220,170,140,0) 80%),
  radial-gradient(ellipse 150px 180px at 135px 330px,rgba(30,34,46,.95),rgba(30,34,46,0) 90%),
  linear-gradient(180deg,rgba(90,110,150,.5),rgba(40,55,90,.2))}
.agent-text{position:absolute;left:427px;top:70px;width:640px;color:#dfe3ec;font-size:11px;line-height:1.75}
.agent-text h2{color:var(--orange);font-size:18px;font-weight:700;text-transform:uppercase;margin-bottom:8px}
.agent-name{color:var(--white);font-weight:700;font-size:15px}
.agent-role{color:#b8bfd0;font-size:11px;font-weight:400;margin-left:6px}
.agent-text p{margin-top:14px}

/* projects */
.projects{position:absolute;left:0;top:1971px;width:1200px;height:584px;background:linear-gradient(180deg,#f4f4f4,#ececec)}
.tile{position:absolute}
.tile::after{content:"";position:absolute;left:0;right:0;bottom:0;height:55%;background:linear-gradient(180deg,rgba(0,0,0,0),rgba(0,0,0,.45))}
.tile-caption{position:absolute;left:16px;bottom:18px;color:var(--white);font-size:11px;width:210px;z-index:1}
.tile-caption h3{font-size:17px;font-weight:700;margin-bottom:4px}
.tile-caption p{color:#e3e3e3;line-height:1.4;font-size:10px}
.tile-btn{margin-top:8px;width:76px;height:20px;border-radius:10px;background:var(--orange);font-size:10px;display:flex;align-items:center;justify-content:center}
.tile-villa{background:linear-gradient(180deg,#7fa9d2 0%,#a9c6e0 22%,#eef0f1 26%,#d9dcde 62%,#3f93c2 66%,#2a7fb0 100%)}
.tile-trees{background:linear-gradient(180deg,#8c9a93 0%,#5d6e63 30%,#c9ccc8 48%,#8e948f 65%,#3c4a3f 100%)}
.tile-classic{background:linear-gradient(180deg,#6f7fb3 0%,#b9a9b8 25%,#ece6da 40%,#d6cdbd 65%,#4e5a3b 80%,#39452c 100%)}
.tile-night{background:linear-gradient(180deg,#1f2128 0%,#2c2d33 25%,#a8733a 45%,#6d4f2c 62%,#1d5b86 80%,#173e5c 100%)}
.wave{position:absolute;left:0;top:2510px}

/* testimonial */
.testimonials{position:absolute;left:0;top:2555px;width:1200px;height:345px;background:var(--white)}
.video{position:absolute;left:149px;top:43px;width:444px;height:268px;background:
  radial-gradient(ellipse 90px 120px at 150px 150px,rgba(200,80,90,.45),rgba(0,0,0,0) 80%),
  radial-gradient(ellipse 90px 120px at 290px 150px,rgba(220,60,60,.45),rgba(0,0,0,0) 80%),
  linear-gradient(180deg,#b5b5b5,#8a8a8a)}
.play{position:absolute;left:200px;top:112px}
.testi-title{position:absolute;left:616px;top:42px;font-family:'Raleway',sans-serif;font-size:22px;font-weight:700}
.quote{position:absolute;left:616px;top:86px;width:444px;height:116px;background:var(--light);padding:18px 24px;font-size:11px;line-height:1.7;color:#666}
.client{position:absolute;left:616px;top:226px;display:flex;align-items:center;gap:14px}
.avatar{width:62px;height:62px;border-radius:50%;background:linear-gradient(180deg,#d8c7b3,#a88e74)}
.client-name{font-family:'Raleway',sans-serif;font-weight:700;font-size:14px}
.client-place{font-size:10px;color:var(--muted);margin:3px 0}

/* footer */
.site-footer{position:absolute;left:0;top:2900px;width:1200px;height:293px;background:var(--footer);color:#888}
.office-title{position:absolute;left:136px;top:55px;color:var(--orange);font-weight:700;font-size:14px;text-transform:uppercase}
.office-info{position:absolute;left:136px;top:82px;font-size:11px;line-height:1.9}
.socials{position:absolute;left:545px;top:70px;display:flex;gap:19px}
.socials span{width:19px;height:19px;border-radius:3px}
.directions{position:absolute;left:918px;top:50px;width:146px;height:38px;border:1px solid #666;border-radius:4px;color:var(--white);font-size:11px;display:flex;align-items:center;justify-content:center;gap:8px}
.footer-phone{position:absolute;left:886px;top:100px;color:var(--orange);font-size:22px;font-weight:700;display:flex;align-items:center;gap:10px}
.footer-rule{position:absolute;left:133px;top:165px;width:934px;height:1px;background:#333}
.footer-links{position:absolute;left:133px;top:184px;display:flex;gap:24px;font-size:10px}
.copyright{position:absolute;right:133px;top:184px;font-size:9px}
</style>
</head>
<body>

<header class="site-header">
  <div class="brand"><span class="brand-mark"></span>Dean Harlow Property</div>
  <nav class="main-nav">
    <a class="active">Home</a><a>For Sale</a><a>Agents</a><a>Book Appraisal</a><a>Contact Us</a>
  </nav>
  <div class="phone-pill">
    <svg width="14" height="14" viewBox="0 0 24 24"><path fill="#fff" d="M6.6 10.8a15 15 0 006.6 6.6l2.2-2.2a1 1 0 011-.25 11.4 11.4 0 003.6.57 1 1 0 011 1V20a1 1 0 01-1 1A17 17 0 013 4a1 1 0 011-1h3.5a1 1 0 011 1c0 1.25.2 2.45.57 3.57a1 1 0 01-.25 1z"/></svg>
    0400 317 628
  </div>
</header>

<section class="hero" role="img" aria-label="Two-storey grey family home at dusk with lit windows">
  <div class="hero-eyebrow">THE BEST REAL ESTATE DEALS</div>
  <h1 class="hero-title">Discover Your Perfect Home</h1>
  <div class="hero-btn">view more</div>
  <svg class="hero-arrow" style="left:114px" width="14" height="24" viewBox="0 0 14 24"><path d="M12 2L2 12l10 10" stroke="#fff" stroke-width="2.5" fill="none"/></svg>
  <svg class="hero-arrow" style="left:1074px" width="14" height="24" viewBox="0 0 14 24"><path d="M2 2l10 10L2 22" stroke="#fff" stroke-width="2.5" fill="none"/></svg>
  <div class="hero-dots"><span></span><span class="on"></span><span></span></div>
</section>

<form class="appraisal">
  <div class="fields">
    <div class="field">Full Name</div><div class="field">E-Mail Address</div><div class="field">Phone Number</div>
    <div class="field">Address</div><div class="field">Preferred Time / Day</div><div class="field">Message</div>
  </div>
  <div class="appraisal-btn">
    <svg width="22" height="22" viewBox="0 0 24 24"><rect x="3" y="3" width="18" height="18" rx="2" stroke="#fff" stroke-width="2" fill="none"/><path d="M7 12l3 3 7-7" stroke="#fff" stroke-width="2" fill="none"/></svg>
    BOOK AN<br>APPRAISAL
  </div>
</form>

<h2 class="section-title" style="top:692px">Properties for sale</h2>

<article class="card" style="left:133px;top:729px">
  <div class="card-photo photo-patio" role="img" aria-label="Modern brick home with covered patio"></div>
  <div class="card-body">
    <div class="card-name">MODERN HOME IN TOP END RIVEVALE!</div>
    <div class="card-price">FROM $ 549,000 – $ 589,000</div>
    <div class="card-addr"><svg width="7" height="9" viewBox="0 0 10 14"><path d="M5 0a5 5 0 00-5 5c0 4 5 9 5 9s5-5 5-9a5 5 0 00-5-5z" fill="#999"/></svg>14 Lindell Street, Rivervale, WA 6105</div>
    <div class="card-feats"><span><svg width="14" height="9"><rect y="3" width="14" height="5" fill="#999"/><rect width="5" height="4" fill="#999"/></svg>3</span><span><svg width="14" height="9"><rect y="3" width="14" height="5" rx="2" fill="#999"/></svg>2</span><span><svg width="14" height="9"><rect y="2" width="14" height="5" rx="2" fill="#999"/><circle cx="3" cy="8" r="1.5" fill="#999"/><circle cx="11" cy="8" r="1.5" fill="#999"/></svg>2</span></div>
    <div class="card-btn">DETAILS &nbsp;›</div>
  </div>
</article>
<article class="card" style="left:611px;top:729px">
  <div class="card-photo photo-white" role="img" aria-label="White two-storey home under blue sky"></div>
  <div class="card-body">
    <div class="card-name">MODERN HOME IN TOP END RIVEVALE!</div>
    <div class="card-price">FROM $ 549,000 – $ 589,000</div>
    <div class="card-addr"><svg width="7" height="9" viewBox="0 0 10 14"><path d="M5 0a5 5 0 00-5 5c0 4 5 9 5 9s5-5 5-9a5 5 0 00-5-5z" fill="#999"/></svg>14 Lindell Street, Rivervale, WA 6105</div>
    <div class="card-feats"><span><svg width="14" height="9"><rect y="3" width="14" height="5" fill="#999"/><rect width="5" height="4" fill="#999"/></svg>3</span><span><svg width="14" height="9"><rect y="3" width="14" height="5" rx="2" fill="#999"/></svg>2</span><span><svg width="14" height="9"><rect y="2" width="14" height="5" rx="2" fill="#999"/><circle cx="3" cy="8" r="1.5" fill="#999"/><circle cx="11" cy="8" r="1.5" fill="#999"/></svg>2</span></div>
    <div class="card-btn">DETAILS &nbsp;›</div>
  </div>
</article>
<article class="card" style="left:133px;top:1104px">
  <div class="card-photo photo-glass" role="img" aria-label="Modern home with glass sliding doors and courtyard"></div>
  <div class="card-body">
    <div class="card-name">MODERN HOME IN TOP END RIVEVALE!</div>
    <div class="card-price">FROM $ 549,000 – $ 589,000</div>
    <div class="card-addr"><svg width="7" height="9" viewBox="0 0 10 14"><path d="M5 0a5 5 0 00-5 5c0 4 5 9 5 9s5-5 5-9a5 5 0 00-5-5z" fill="#999"/></svg>14 Lindell Street, Rivervale, WA 6105</div>
    <div class="card-feats"><span><svg width="14" height="9"><rect y="3" width="14" height="5" fill="#999"/><rect width="5" height="4" fill="#999"/></svg>3</span><span><svg width="14" height="9"><rect y="3" width="14" height="5" rx="2" fill="#999"/></svg>2</span><span><svg width="14" height="9"><rect y="2" width="14" height="5" rx="2" fill="#999"/><circle cx="3" cy="8" r="1.5" fill="#999"/><circle cx="11" cy="8" r="1.5" fill="#999"/></svg>2</span></div>
    <div class="card-btn">DETAILS &nbsp;›</div>
  </div>
</article>
<article class="card" style="left:611px;top:1104px">
  <div class="card-photo photo-kitchen" role="img" aria-label="Bright open-plan kitchen and living room"></div>
  <div class="card-body">
    <div class="card-name">MODERN HOME IN TOP END RIVEVALE!</div>
    <div class="card-price">FROM $ 549,000 – $ 589,000</div>
    <div class="card-addr"><svg width="7" height="9" viewBox="0 0 10 14"><path d="M5 0a5 5 0 00-5 5c0 4 5 9 5 9s5-5 5-9a5 5 0 00-5-5z" fill="#999"/></svg>14 Lindell Street, Rivervale, WA 6105</div>
    <div class="card-feats"><span><svg width="14" height="9"><rect y="3" width="14" height="5" fill="#999"/><rect width="5" height="4" fill="#999"/></svg>3</span><span><svg width="14" height="9"><rect y="3" width="14" height="5" rx="2" fill="#999"/></svg>2</span><span><svg width="14" height="9"><rect y="2" width="14" height="5" rx="2" fill="#999"/><circle cx="3" cy="8" r="1.5" fill="#999"/><circle cx="11" cy="8" r="1.5" fill="#999"/></svg>2</span></div>
    <div class="card-btn">DETAILS &nbsp;›</div>
  </div>
</article>

<div class="load-more">LOAD MORE</div>

<section class="agent">
  <div class="agent-photo" role="img" aria-label="Portrait of agent in suit and striped tie"></div>
  <div class="agent-text">
    <h2>Agents</h2>
    <div class="agent-name">Dean Harlow<span class="agent-role">Sales Partner</span></div>
    <p>Raised in Perth from day one, Dean has approached his career in real estate with an ambition of building lasting relationships based on trust, confidence and integrity. Over a long period of time his experiences have consistently validated this attitude with Dean enjoying an abundance of referrals and repeat business throughout the Perth metropolitan market, from mid-high end residential property and residential land based developments.</p>
    <p>Having operated his real estate practice since 2009, Dean prides himself on having excellent communication skills, a diligent nature and a highly professional manner. The tenacity and integrity that has fostered his enviable reputation has also gained Dean respect and trust amongst his peers.</p>
    <p>Dean has achieved many milestones in his life, his most significant was becoming a father to a son of whom he says is his 'why' in life. Dean also has a very keen focus on health and wellness having personally created lasting changes and has assisted people in becoming their best self.</p>
  </div>
</section>

<section class="projects">
  <h2 class="section-title" style="top:36px">Featured projects</h2>
  <div class="tile tile-villa" role="img" aria-label="White modern villa with pool" style="left:136px;top:82px;width:577px;height:214px">
    <div class="tile-caption"><h3>Studio Arden</h3><p>Lorem ipsum dolor sit amet, consectetuer adipiscing elit, aenean commodo ligula.</p></div>
  </div>
  <div class="tile tile-trees" role="img" aria-label="Contemporary house among trees" style="left:733px;top:82px;width:334px;height:214px">
    <div class="tile-caption"><h3>Studio Arden</h3><p>Lorem ipsum dolor sit amet, consectetuer adipiscing elit, aenean commodo ligula.</p><div class="tile-btn">view more</div></div>
  </div>
  <div class="tile tile-classic" role="img" aria-label="Classic weatherboard home at sunset" style="left:136px;top:309px;width:577px;height:209px">
    <div class="tile-caption"><h3>Studio Arden</h3><p>Lorem ipsum dolor sit amet, consectetuer adipiscing elit, aenean commodo ligula.</p></div>
  </div>
  <div class="tile tile-night" role="img" aria-label="Modern house lit at night beside pool" style="left:733px;top:309px;width:334px;height:209px">
    <div class="tile-caption"><h3>Studio Arden</h3><p>Lorem ipsum dolor sit amet, consectetuer adipiscing elit, aenean commodo ligula.</p></div>
  </div>
</section>
<svg class="wave" width="1200" height="46" viewBox="0 0 1200 46"><path d="M0 46V30Q300 0 600 22T1200 10V46z" fill="#fff"/></svg>

<section class="testimonials">
  <div class="video" role="img" aria-label="Happy couple holding a house sign">
    <svg class="play" width="44" height="44" viewBox="0 0 44 44"><circle cx="22" cy="22" r="19" fill="none" stroke="#fff" stroke-width="3"/><path d="M17 13l13 9-13 9z" fill="#fff"/></svg>
  </div>
  <h2 class="testi-title">2000+ Happy Clients</h2>
  <div class="quote">Harlow Realty has recently sold our house and home. We have found that it was one of the best investments we could have made, as nothing was a problem to her, and it certainly took the worry of marketing and selling off our mind, as Harlow Realty had everyone under control.</div>
  <div class="client">
    <div class="avatar" role="img" aria-label="Client couple photo"></div>
    <div>
      <div class="client-name">Sophie &amp; Mark</div>
      <div class="client-place">Eastfield, Hawthorne</div>
      <svg width="60" height="10" viewBox="0 0 60 10"><g fill="#f3a40f"><path id="s" d="M5 0l1.5 3.2 3.5.4-2.6 2.4.7 3.5L5 7.8 1.9 9.5l.7-3.5L0 3.6l3.5-.4z"/><use href="#s" x="12"/><use href="#s" x="24"/><use href="#s" x="36"/><use href="#s" x="48"/></g></svg>
    </div>
  </div>
</section>

<footer class="site-footer">
  <div class="office-title">Visit our office</div>
  <div class="office-info">88 Carrow Lane, Westbrook, WA 6012<br>Mon – Sat : 10 am – 6 pm &nbsp;|&nbsp; Sun : 12 pm – 2 pm</div>
  <div class="socials" aria-label="Social links">
    <span style="background:#3b5a9a"></span><span style="background:#2a9fd8"></span><span style="background:#e8822a"></span><span style="background:#d2432f"></span><span style="background:#4a90c8"></span>
  </div>
  <div class="directions">
    <svg width="12" height="14" viewBox="0 0 10 14"><path d="M5 0a5 5 0 00-5 5c0 4 5 9 5 9s5-5 5-9a5 5 0 00-5-5z" fill="#fff"/></svg>Get Directions
  </div>
  <div class="footer-phone">
    <svg width="22" height="22" viewBox="0 0 24 24"><path fill="#f36c0f" d="M6.6 10.8a15 15 0 006.6 6.6l2.2-2.2a1 1 0 011-.25 11.4 11.4 0 003.6.57 1 1 0 011 1V20a1 1 0 01-1 1A17 17 0 013 4a1 1 0 011-1h3.5a1 1 0 011 1c0 1.25.2 2.45.57 3.57a1 1 0 01-.25 1z"/></svg>
    0400 317 628
  </div>
  <div class="footer-rule"></div>
  <nav class="footer-links"><a>Home</a><a>Furniture</a><a>Lighting</a><a>Decor</a><a>Gifts</a><a>Textiles</a><a>About me</a><a>Contact me</a></nav>
  <div class="copyright">Copyright © 2018 DEANHARLOWPROPERTY-EXAMPLE.COM. All Rights Reserved</div>
</footer>

</body>
</html>
```